need a Flyer for Plush Toy company

Need a Flyer for Plush Toy company ,

I upload a file for TEXT

Target Market(s)

Toys wholesalers , Supermarket

Industry/Entity Type

Toy Store

Colors
000000
ec1f27
c4c4c4

Requirements
Must have
• I have up loaded 3 files
• 1. Logo Registered Brand
• 2. customer's design in drawing
• 3. our ready samples based on Design
Nice to have
• happy kids in Nature ,
• happy kids in Ski ,
• different color Kids ,
• Multi culture concept

```html
<!DOCTYPE html>
<html lang="en">
<head>
<meta charset="utf-8">
<title>Lumo Nest – Plush Toy Flyer</title>
<link rel="stylesheet" href="https://fonts.googleapis.com/css2?family=Delius&family=Roboto+Condensed:wght@500;700&family=Arimo:ital,wght@1,700&display=swap">
<style>
  :root{
    --black:#000000;
    --red:#ec1f27;
    --grey:#c4c4c4;
    --deep-red:#6e0b10;
    --white:#ffffff;
    --box:#dcdcdc;
  }
  *{margin:0;padding:0;box-sizing:border-box}
  html,body{width:902px;height:1200px;overflow:hidden;background:var(--white)}
  .flyer{position:relative;width:902px;height:1200px;overflow:hidden;background:var(--white)}
  .flyer-shapes{position:absolute;inset:0;width:902px;height:1200px}
  .text{position:absolute;white-space:nowrap}

  .brand-mark{left:120px;top:128px;display:flex;align-items:center;gap:12px;
    font-family:"Delius",cursive;font-size:40px;color:var(--black)}
  .brand-mark .dot{width:22px;height:22px;border-radius:50%;background:var(--red)}
  .tagline{left:48px;top:246px;font-family:"Delius",cursive;font-size:31px;color:var(--red)}

  .company-name{left:92px;top:414px;font-family:"Delius",cursive;font-size:84px;color:var(--white);letter-spacing:1px}
  .business-type{left:42px;top:512px;font-family:"Roboto Condensed",sans-serif;font-weight:700;font-size:24.5px;color:var(--red)}
  .offer{font-family:"Roboto Condensed",sans-serif;font-weight:700;font-size:25px;color:var(--white)}
  .offer-one{left:92px;top:544px}
  .offer-two{left:132px;top:580px}

  .facts{position:absolute;left:46px;top:672px;width:630px;list-style:none;
    font-family:"Arimo",sans-serif;font-style:italic;font-weight:700;font-size:14px;line-height:17.5px;color:var(--white)}
  .facts li{position:relative;padding-left:21px;margin-bottom:4px}
  .facts li::before{content:"";position:absolute;left:0;top:4px;width:9px;height:9px;border-radius:50%;background:var(--black)}
  .premium-note{left:136px;top:830px;font-family:"Arimo",sans-serif;font-style:italic;font-weight:700;font-size:19.5px;line-height:24px;color:var(--deep-red)}

  .address{left:54px;top:930px;font-family:"Delius",cursive;font-size:18px;color:var(--red)}
  .contact{position:absolute;left:54px;top:966px;font-family:"Delius",cursive;font-size:13.5px;line-height:16.6px;color:var(--white)}
  .bank-box{position:absolute;left:0;top:1070px;width:458px;height:92px;background:var(--box);opacity:.93}
  .bank-title{left:54px;top:1074px;font-family:"Delius",cursive;font-size:17px;color:var(--red)}
  .bank-lines{position:absolute;left:54px;top:1096px;font-family:"Delius",cursive;font-size:14px;line-height:17.5px;color:#222}
</style>
</head>
<body>
<main class="flyer">
  <svg class="flyer-shapes" viewBox="0 0 902 1200" aria-hidden="false">
    <defs>
      <linearGradient id="lower-scene" x1="0" y1="0" x2="1" y2="0">
        <stop offset="0" stop-color="#1c2a3e"/>
        <stop offset="0.45" stop-color="#33557e"/>
        <stop offset="1" stop-color="#7fc0ec"/>
      </linearGradient>
      <linearGradient id="top-scene" x1="0" y1="0" x2="1" y2="1">
        <stop offset="0" stop-color="#4f8f2c"/>
        <stop offset="0.6" stop-color="#e3b89a"/>
        <stop offset="1" stop-color="#2f6b1e"/>
      </linearGradient>
      <linearGradient id="toys-scene" x1="0" y1="0" x2="1" y2="0">
        <stop offset="0" stop-color="#f3c7d6"/>
        <stop offset="0.5" stop-color="#c9b8e6"/>
        <stop offset="1" stop-color="#f4e07a"/>
      </linearGradient>
    </defs>

    <rect class="lower-photo" x="0" y="540" width="902" height="660" fill="url(#lower-scene)" role="img" aria-label="Photo: happy children of many backgrounds cheering with raised arms in a sunny meadow"/>
    <rect x="0" y="1162" width="458" height="38" fill="#16341c"/>

    <rect class="top-photo" x="340" y="0" width="562" height="470" fill="url(#top-scene)" role="img" aria-label="Photo: smiling boy eating a pea pod in a green garden"/>
    <path class="white-corner" d="M0 0 H362 C378 140 410 260 470 330 C500 362 520 372 540 380 L0 380 Z" fill="var(--white)"/>

    <path class="red-shape" d="M0 590 H560 C700 590 770 690 770 780 C770 875 650 915 480 920 C300 926 150 920 0 926 Z" fill="var(--red)"/>
    <path class="red-line" d="M0 346 C250 322 450 372 620 402 C740 422 840 418 902 393" fill="none" stroke="var(--red)" stroke-width="4"/>
    <path class="black-band" d="M0 354 C250 332 450 382 620 412 C740 432 840 426 902 402 V470 C790 468 650 500 605 560 C570 610 500 632 400 632 H0 Z" fill="var(--black)"/>

    <ellipse cx="745" cy="583" rx="236" ry="134" fill="var(--white)"/>
    <ellipse class="samples-photo" cx="745" cy="583" rx="228" ry="126" fill="url(#toys-scene)" role="img" aria-label="Photo: row of pastel plush toy samples"/>
  </svg>

  <div class="text brand-mark"><span class="dot"></span>Lumo Nest</div>
  <p class="text tagline">Have you been there?</p>

  <h1 class="text company-name">Lumo Nest</h1>
  <p class="text business-type">EINZELUNTERNEHMEN / FAMILY BUSINESS</p>
  <p class="text offer offer-one">Innovative Developer&nbsp; for Plush Toys</p>
  <p class="text offer offer-two">International Trader for Toys</p>

  <ul class="facts">
    <li>We live and work in Talheim near to Cologne Germany.</li>
    <li>We speak German and English.</li>
    <li>The toys are made in China, we are small family business , but we are professional in Plush toys business , right now we have successfully&nbsp; launched Projects with a huge Japanese 100 Yen Chain Store.&nbsp; Here in Flyer we show a Sample project.</li>
    <li>100 Yen = 0.90 USD&nbsp; , Our products can meet strictest Quality Control , but are with extremely Low Price to fit for&nbsp; Japanese Dollar Shop as well as his overseas Store around the world.</li>
  </ul>
  <p class="text premium-note">OF COURSE OUR PRODUCTS ARE FIT FOR<br>PREMIUM STORE TOO.</p>

  <p class="text address">Lindenweg 8, 50999 Talheim Germany</p>
  <div class="contact">
    hello@lumonest.de<br>
    Fon&nbsp;&nbsp;&nbsp; +49 (0)&nbsp; 2200- 555 0140<br>
    Fax&nbsp;&nbsp;&nbsp; +49 (0)&nbsp; 2200- 555 0141<br>
    Mobil:&nbsp; +49 (0) 170 5550 182<br>
    Ust-IdNr./VAT No. DE000111222
  </div>

  <div class="bank-box"></div>
  <p class="text bank-title">Bank information :</p>
  <div class="bank-lines">
    Kontoinhaber/Account Holder:&nbsp;&nbsp; Mei Lin<br>
    IBAN:&nbsp; DE00 1234 5678 9012 3456 78<br>
    BIC : BANKDEXX000
  </div>
</main>
</body>
</html>
```